Kelvora Energy Brochure

This will be an 8 page brochure 8.5 X 11" Page Order: Front Cover, Solar, Storage, O&M, Automated Cleaning Systems, Electrical, Roofing, Back Cover. Most information needed can be found on our website. Ask for anything you need.

Target Market(s)

Commercial Solar Customers, Roofing Customers

Industry/Entity Type

Renewable Energy

Font styles to use
Serif

Colors
0054AA
0677BA
7BADD7
CADEEF
E8F1F8

```html
<!DOCTYPE html>
<html lang="en">
<head>
<meta charset="utf-8">
<title>Kelvora Energy Brochure</title>
<link href="https://fonts.googleapis.com/css2?family=Montserrat:wght@300;400;500;600;700;800&display=swap" rel="stylesheet">
<style>
:root{
  --bg:#e2e2e2;
  --paper:#ffffff;
  --blue:#0054aa;
  --blue-mid:#0677ba;
  --blue-dark:#1f5f8b;
  --blue-light:#7badd7;
  --blue-pale:#cadeef;
  --green:#6cbd45;
  --ink:#2b2b2b;
  --muted:#6b6b6b;
}
*{box-sizing:border-box;margin:0;padding:0}
html,body{width:1200px;height:4000px;overflow:hidden;background:var(--bg)}
body{position:relative;font-family:"Montserrat",Arial,sans-serif;color:var(--ink)}
.page{position:absolute;left:335px;width:528px;height:683px;background:var(--paper);box-shadow:0 2px 8px rgba(0,0,0,.12);overflow:hidden}
.abs{position:absolute}
.brand{font-family:"Montserrat",Arial,sans-serif;font-weight:700;color:var(--blue);letter-spacing:.2px;white-space:nowrap}

/* cover */
.cover .brand{left:0;right:0;top:52px;text-align:center;font-size:26px}
.cover-band{left:0;top:115px;width:528px;height:9px;background:var(--blue)}
.cover-photo{left:0;top:124px;width:528px;height:370px;background:linear-gradient(135deg,#9aa6b2 0%,#5f6b77 45%,#2f3740 70%,#7d8893 100%)}
.cover-green{left:0;top:478px;width:528px;height:32px;background:var(--green)}
.cover-green-tab{left:150px;top:466px;width:230px;height:14px;background:var(--green);clip-path:polygon(6% 0,94% 0,100% 100%,0 100%)}
.cover-title{left:0;right:0;top:532px;text-align:center}
.cover-title .light{display:block;font-weight:300;font-size:28px;color:#333;line-height:1}
.cover-title .bold{display:block;font-weight:800;font-size:31px;color:var(--blue);line-height:1.05}
.cover-address{left:0;right:0;top:601px;text-align:center;font-size:10.5px;font-weight:600;color:#222}
.cover-url{left:0;right:0;top:622px;text-align:center;font-size:11.5px;font-weight:600;letter-spacing:2.4px;color:#222}

/* contents */
.toc-head{left:0;top:84px;height:34px;display:flex;align-items:center;white-space:nowrap}
.toc-head .tab{height:34px;background:var(--green);display:flex;align-items:center;padding:0 2px 0 36px;font-size:28px;font-weight:300;color:#fff;white-space:nowrap}
.toc-head .strong{font-size:28px;font-weight:800;color:var(--blue);padding-left:6px}
.toc-item{left:40px;width:450px}
.toc-item .label{position:absolute;left:0;font-size:17px;font-weight:700;color:var(--blue);line-height:1.2}
.toc-item .rule{position:absolute;left:0;width:424px;border-top:1.5px dotted #555}
.num{position:absolute;width:26px;height:25px;background:var(--green);color:#fff;font-size:12px;font-weight:600;display:flex;align-items:center;justify-content:center}
.toc-foot-brand{left:37px;top:603px;font-size:22px}
.toc-foot-url{right:39px;top:611px;font-size:11.5px;color:#333}

/* shared heading */
.head{left:37px;border-left:6px solid var(--green);padding-left:12px;line-height:1;white-space:nowrap}
.head .light{font-weight:300;color:#333}
.head .bold{font-weight:800;color:var(--blue)}

/* footer */
.foot-brand{left:45px;top:620px;font-size:22px}
.foot-line{left:140px;top:640px;width:324px;height:1px;background:var(--blue-light)}
.foot-url{right:70px;top:625px;font-size:9px;color:#444}
.foot-num{right:36px;top:624px;width:28px;height:16px;background:var(--blue-mid);color:#fff;font-size:10px;font-weight:700;display:flex;align-items:center;justify-content:center;clip-path:polygon(18% 0,100% 0,100% 100%,0 100%)}

/* profile */
.profile-head{top:56px;font-size:27px}
.copy{left:37px;width:455px;font-size:7.6px;line-height:1.45;color:#333}
.copy p{margin-bottom:8px}
.copy strong{font-weight:700;color:#111}
.stat{top:300px;width:147px;height:129px;color:#fff;padding:16px 18px}
.stat-green{left:37px;background:var(--green)}
.stat-blue{left:185px;background:var(--blue);text-align:center;padding-left:0;padding-right:20px}
.stat .big{font-size:36px;font-weight:800;line-height:1}
.stat .small{font-size:11.5px;font-weight:700;line-height:1.2;margin-top:8px}
.stat-blue .big{font-size:32px;margin-top:6px}
.stat-blue .small{margin-top:14px}
.map{left:29px;top:455px;width:256px;height:121px;background:linear-gradient(90deg,#1f7fc0,#2c8fcf);border-radius:40px 60px 30px 50px}
.profile-photo{left:342px;top:300px;width:150px;height:290px;background:linear-gradient(180deg,#5b6570 0%,#c9ced4 40%,#8e969e 65%,#3e454c 100%)}

/* solution */
.sol-head{top:47px;font-size:24px}
.sol-head .light,.sol-head .bold{display:block}
.sol-head .bold{margin-top:2px}
.sol-sub{left:40px;top:128px;width:440px;font-size:15.5px;font-weight:700;color:#111;line-height:1.3}
.sol-note{left:40px;top:173px;width:450px;font-size:7.4px;color:#333;line-height:1.4}
.feature{top:250px;width:151px;height:144px;color:#fff;padding:14px 14px 0 17px}
.feature h3{font-size:11.5px;font-weight:700;line-height:1.25;margin-bottom:6px}
.feature p{font-size:6.8px;line-height:1.45;color:#e8f1f8}
.f1{left:37px;background:var(--blue-dark)}
.f2{left:188px;background:var(--blue-mid)}
.f3{left:339px;width:152px;background:var(--blue-dark)}
.f2 h3{margin-bottom:10px}
.icon{top:198px;width:54px;height:54px;border-radius:50%;background:var(--blue);border:3px solid #fff;box-shadow:0 0 0 1px var(--blue)}
.sol-photo{left:37px;top:415px;width:210px;height:171px;background:linear-gradient(120deg,#1e2a36 0%,#56646f 50%,#a6b0b8 100%)}
.partner{left:247px;top:415px;width:244px;height:171px;background:var(--green);color:#fff;padding:12px 20px 0 34px}
.partner h3{font-size:13px;font-weight:700;line-height:1.3;margin-bottom:10px}
.partner ul{list-style:none}
.partner li{font-size:9.5px;font-weight:600;line-height:1;margin-bottom:9px;display:flex;align-items:center;gap:8px}
.partner li svg{flex:none}
.sol-foot-brand{left:37px;top:614px}

/* back */
.back-brand{left:45px;top:588px;font-size:22px}
.contact{left:235px;font-size:11.5px;color:#222;display:flex;align-items:center;gap:13px;white-space:nowrap}
.contact.phone{top:564px;font-size:19px;font-weight:700;color:#111}
.contact svg{flex:none}
</style>
</head>
<body>

<!-- Front cover -->
<section class="page cover" style="top:174px">
  <div class="abs brand">Kelvora Energy</div>
  <div class="abs cover-band"></div>
  <div class="abs cover-photo" role="img" aria-label="Close-up photo of a rotating sprinkler head spraying water across a solar panel frame"></div>
  <div class="abs cover-green-tab"></div>
  <div class="abs cover-green"></div>
  <h1 class="abs cover-title"><span class="light">AUTOMATED</span><span class="bold">CLEANING SYSTEMS</span></h1>
  <p class="abs cover-address">KELVORA ENERGY 1480 Orchard Ln Ripon, CA 95366</p>
  <p class="abs cover-url">www.kelvoraenergy.com</p>
</section>

<!-- Table of contents -->
<section class="page toc" style="top:916px">
  <h2 class="abs toc-head"><span class="tab">TABLE OF</span><span class="strong">CONTENTS</span></h2>

  <div class="abs toc-item" style="top:180px"><span class="label" style="top:0">Solar</span><span class="rule" style="top:34px"></span><span class="num" style="left:424px;top:7px">01</span></div>
  <div class="abs toc-item" style="top:233px"><span class="label" style="top:0">Storage</span><span class="rule" style="top:40px"></span><span class="num" style="left:424px;top:14px">02</span></div>
  <div class="abs toc-item" style="top:285px"><span class="label" style="top:0">O&amp;M</span><span class="rule" style="top:44px"></span><span class="num" style="left:424px;top:18px">03</span></div>
  <div class="abs toc-item" style="top:338px"><span class="label" style="top:0">Automated<br>Cleaning Systems</span><span class="rule" style="top:47px"></span><span class="num" style="left:424px;top:21px">04</span></div>
  <div class="abs toc-item" style="top:415px"><span class="label" style="top:0">Electrical</span><span class="rule" style="top:31px"></span><span class="num" style="left:424px;top:5px">05</span></div>
  <div class="abs toc-item" style="top:470px"><span class="label" style="top:0">Roofing</span><span class="rule" style="top:33px"></span><span class="num" style="left:424px;top:7px">06</span></div>

  <div class="abs brand toc-foot-brand">Kelvora Energy</div>
  <div class="abs toc-foot-url">www.kelvoraenergy.com</div>
</section>

<!-- Company profile -->
<section class="page profile" style="top:1658px">
  <h2 class="abs head profile-head"><span class="light">COMPANY </span><span class="bold">PROFILE</span></h2>
  <div class="abs copy" style="top:110px">
    <p>Kelvora Energy (Kelvora) specializes in automated solar panel cleaning systems for commercial, industrial, agricultural, and utility scale projects. Our systems preserve panel warranties and increase solar production. We do this by cleaning at night with low pressure soft water using advanced water engineering.</p>
    <p><strong>We provide the first economical solution to eliminating soiling losses.</strong></p>
    <p>Automated Cleaning Systems have been installed since 2011 and today, there are over 4,000 systems installed worldwide on a total of over 1.5 GW of panels with systems ranging in size from large utility projects to cleaning systems for residential solar arrays. On average, we clean over 1,000,000 panels every day.</p>
    <p>Automated Cleaning Systems also decrease secondary<br>costs such as roof damage from personnel walking on the roof while washing the panels.</p>
    <p>Our goal is to optimize your solar production through constant cleaning, and regular proactive maintenance.</p>
  </div>
  <div class="abs stat stat-green"><div class="big">4,000</div><div class="small">Projects installed<br>(on over 1.5 GW<br>of panels)</div></div>
  <div class="abs stat stat-blue"><div class="big">6</div><div class="small">worldwide<br>locations</div></div>
  <div class="abs map" role="img" aria-label="World map in blue with green markers on six office locations"></div>
  <div class="abs profile-photo" role="img" aria-label="Photo of a sprinkler spraying a fan of water over solar panels"></div>
  <div class="abs brand foot-brand" style="top:614px">Kelvora Energy</div>
  <div class="abs foot-line"></div>
  <div class="abs foot-url">www.kelvoraenergy.com</div>
  <div class="abs foot-num">01</div>
</section>

<!-- Cleaning solution -->
<section class="page solution" style="top:2400px">
  <h2 class="abs head sol-head"><span class="light">AUTOMATED SOLAR PANEL</span><span class="bold">CLEANING SOLUTION</span></h2>
  <p class="abs sol-sub">Your existing solar system could be producing up to 30% more energy.</p>
  <p class="abs sol-note">The system uses two separate water filter technologies to ensure only the cleanest water is used. This helps to prevent harmful water scaling and corrosion!</p>

  <div class="abs feature f1"><h3>Automatic Nightly<br>Cleaning</h3><p>The system cleans regularly at night, keeping the panels consistently clean, preventing dirt and limescale buildup – thus increasing energy production by upwards of 30%.</p></div>
  <div class="abs feature f2"><h3>Safe &amp; Efficient</h3><p>The system distributes water through an automated, reliable system – reducing labor, safety hazards and damage to rooftops. No chemicals or abrasive brushes are used. Utilizing a 'self-maintenance' protocol, the system helps you achieve the lowest operating costs possible.</p></div>
  <div class="abs feature f3"><h3>Warranty<br>Compliant</h3><p>The system cleans the panels at night to avoid thermal stress to the module glass. By keeping the modules clean on a constant basis and not using abrasive brushes or solvents you can ensure warranty compliance with your module manufacturer.</p></div>

  <div class="abs icon" style="left:86px"><svg width="48" height="48" viewBox="0 0 48 48"><rect x="16" y="13" width="16" height="22" rx="2" fill="none" stroke="#fff" stroke-width="2"/><path d="M20 22a5 5 0 0 1 8 0M22 25a2 2 0 0 1 4 0" fill="none" stroke="#fff" stroke-width="1.6"/></svg></div>
  <div class="abs icon" style="left:235px"><svg width="48" height="48" viewBox="0 0 48 48"><path d="M24 11l11 4v8c0 7-5 12-11 14-6-2-11-7-11-14v-8z" fill="none" stroke="#fff" stroke-width="2"/><path d="M19 24l4 4 7-7" fill="none" stroke="#fff" stroke-width="2"/></svg></div>
  <div class="abs icon" style="left:378px"><svg width="48" height="48" viewBox="0 0 48 48"><rect x="15" y="11" width="16" height="22" rx="1.5" fill="none" stroke="#fff" stroke-width="2"/><path d="M19 17h8M19 21h8M19 25h5" stroke="#fff" stroke-width="1.6"/><circle cx="31" cy="32" r="6" fill="#fff"/><path d="M28 32l2 2 4-4" fill="none" stroke="#0054aa" stroke-width="1.6"/></svg></div>

  <div class="abs sol-photo" role="img" aria-label="Photo of a sprinkler head spraying water over a solar panel at dusk"></div>
  <div class="abs partner">
    <h3>Consider us your long-term<br>energy partners.</h3>
    <ul>
      <li><svg width="9" height="9" viewBox="0 0 10 10"><circle cx="5" cy="5" r="4.3" fill="none" stroke="#fff" stroke-width="1"/><path d="M3 5l1.5 1.5L7 4" fill="none" stroke="#fff" stroke-width="1"/></svg>Increase Production</li>
      <li><svg width="9" height="9" viewBox="0 0 10 10"><circle cx="5" cy="5" r="4.3" fill="none" stroke="#fff" stroke-width="1"/><path d="M3 5l1.5 1.5L7 4" fill="none" stroke="#fff" stroke-width="1"/></svg>Robust Technology</li>
      <li><svg width="9" height="9" viewBox="0 0 10 10"><circle cx="5" cy="5" r="4.3" fill="none" stroke="#fff" stroke-width="1"/><path d="M3 5l1.5 1.5L7 4" fill="none" stroke="#fff" stroke-width="1"/></svg>Remotely Controlled</li>
      <li><svg width="9" height="9" viewBox="0 0 10 10"><circle cx="5" cy="5" r="4.3" fill="none" stroke="#fff" stroke-width="1"/><path d="M3 5l1.5 1.5L7 4" fill="none" stroke="#fff" stroke-width="1"/></svg>Safer Cleaning</li>
      <li><svg width="9" height="9" viewBox="0 0 10 10"><circle cx="5" cy="5" r="4.3" fill="none" stroke="#fff" stroke-width="1"/><path d="M3 5l1.5 1.5L7 4" fill="none" stroke="#fff" stroke-width="1"/></svg>Protects Solar Panel Warranty</li>
      <li><svg width="9" height="9" viewBox="0 0 10 10"><circle cx="5" cy="5" r="4.3" fill="none" stroke="#fff" stroke-width="1"/><path d="M3 5l1.5 1.5L7 4" fill="none" stroke="#fff" stroke-width="1"/></svg>Proven Technology</li>
    </ul>
  </div>
  <div class="abs brand foot-brand sol-foot-brand">Kelvora Energy</div>
  <div class="abs foot-line"></div>
  <div class="abs foot-url">www.kelvoraenergy.com</div>
  <div class="abs foot-num">01</div>
</section>

<!-- Back cover -->
<section class="page back" style="top:3143px">
  <div class="abs brand back-brand">Kelvora Energy</div>
  <div class="abs contact phone"><svg width="12" height="12" viewBox="0 0 24 24"><path d="M6.6 10.8a15 15 0 0 0 6.6 6.6l2.2-2.2c.3-.3.7-.4 1-.2 1.1.4 2.3.6 3.6.6.6 0 1 .4 1 1V20c0 .6-.4 1-1 1A17 17 0 0 1 3 4c0-.6.4-1 1-1h3.5c.6 0 1 .4 1 1 0 1.3.2 2.5.6 3.6.1.3 0 .7-.2 1z" fill="#0054aa"/></svg>555.014.2270</div>
  <div class="abs contact" style="top:594px"><svg width="12" height="12" viewBox="0 0 24 24"><rect x="2" y="5" width="20" height="14" rx="2" fill="#0054aa"/><path d="M3 6l9 7 9-7" fill="none" stroke="#fff" stroke-width="1.6"/></svg>dana.marsh@kelvoraenergy.com</div>
  <div class="abs contact" style="top:617px"><svg width="12" height="12" viewBox="0 0 24 24"><circle cx="12" cy="12" r="9.5" fill="none" stroke="#0054aa" stroke-width="2"/><path d="M2.5 12h19M12 2.5c3 3 3 16 0 19M12 2.5c-3 3-3 16 0 19" fill="none" stroke="#0054aa" stroke-width="1.6"/></svg>www.kelvoraenergy.co</div>
</section>

</body>
</html>
```